2 guided dives on the North of Bonaire

2 guided shore dives on the North of Bonaire including authentic local lunch and drinks.
We offer an adventure for experienced divers to discover the dive sites on the north of the island.
Showing you the beauty of the reefs and tasting authentic local cuisine like goat or iguana combined with a stunning view of the surroundings.

Target Market(s)

Divers / tourism

Industry/Entity Type

Tourism / Diving

Font styles to use
Sans Serif

Colors
0054AA
0677BA
7BADD7
CADEEF
E8F1F8
0094D4
00A9DD
6FCCEA
C7EBF8
E9F6FB
F0912C
F2A743
F7CA91
FBE8D2
FDF5EE
EE7325
F08F49
F5BC92
FAE3D3
FDF4ED

Requirements
Must have
• Some of the pictures I uploaded and the food picture / bottom like in the pictures
Nice to have
• inviting to join us on the guided dives
Should not have
• Any picture I didn't provide

```html
<!DOCTYPE html>
<html lang="en">
<head>
<meta charset="utf-8">
<title>Reef Trail Divers – Guided Dives Flyer</title>
<link href="https://fonts.googleapis.com/css2?family=Poppins:ital,wght@0,400;0,500;0,600;0,700;0,800;1,600;1,700;1,900&display=swap" rel="stylesheet">
<style>
:root{
  --board:#e6e6e6;
  --label:#333333;
  --navy:#262a55;
  --blue-deep:#0054aa;
  --blue:#0677ba;
  --blue-bright:#0094d4;
  --blue-sky:#00a9dd;
  --blue-soft:#6fccea;
  --blue-bar:#3b8fc0;
  --orange:#f0912c;
  --orange-warm:#f2a743;
  --white:#ffffff;
}
*{margin:0;padding:0;box-sizing:border-box}
html,body{width:1200px;height:3448px;overflow:hidden}
body{background:var(--board);font-family:'Poppins',sans-serif;position:relative}
.side-label{position:absolute;left:0;width:1200px;text-align:center;font-weight:800;font-size:68px;color:var(--label);letter-spacing:1px;line-height:1}
.side-label.front{top:36px}
.side-label.back{top:1704px}

.flyer{position:absolute;left:86px;width:1028px;height:1443px;overflow:hidden;background:var(--blue);box-shadow:0 14px 16px rgba(0,0,0,.35)}
.flyer.front{top:141px}
.flyer.back{top:1838px}

.hero-photo{position:absolute;left:0;top:0;width:1028px;height:660px}
.front .hero-photo{background:linear-gradient(180deg,#3d78c4 0%,#8fb4df 28%,#6d7d58 40%,#3f5a36 47%,#3f7ab8 56%,#2e69a8 75%,#5a6e3c 100%)}
.back .hero-photo{background:linear-gradient(180deg,#5a4326 0%,#7b5f3a 14%,#5a8fd6 26%,#8cb6e6 50%,#4fb7c9 66%,#d9ccb4 84%,#e8dfcc 100%)}

.wave{position:absolute;left:0;top:0;width:1028px;height:1443px}

.photo-circle{position:absolute;border-radius:50%;border:7px solid var(--white);box-shadow:0 6px 14px rgba(0,0,0,.3)}
.photo-circle.small{left:202px;top:306px;width:286px;height:286px}
.front .photo-circle.small{background:linear-gradient(180deg,#3e78c9 0%,#9bc0e6 45%,#1f8fae 58%,#7b7568 75%,#a69a86 100%)}
.back .photo-circle.small{background:radial-gradient(circle at 60% 55%,#a27450 0%,#6a3b34 30%,#1d5d73 60%,#0f3e56 100%)}
.photo-circle.food{left:586px;top:837px;width:402px;height:402px;border-width:8px;background:radial-gradient(circle at 50% 55%,#c87a3a 0%,#a45a2c 35%,#6b3b22 65%,#3a2a20 100%)}

.badge{position:absolute;left:822px;top:31px;width:174px;height:174px;border-radius:50%;background:var(--white);box-shadow:0 4px 10px rgba(0,0,0,.2)}
.badge::after{content:"";position:absolute;left:50px;top:42px;width:74px;height:74px;border-radius:50%;background:var(--blue-bright)}

.brand-circle{position:absolute;left:539px;top:472px;width:322px;height:322px;border-radius:50%;background:var(--white);border:8px solid var(--blue-deep);box-shadow:0 6px 16px rgba(0,0,0,.35);text-align:center}
.brand-circle .brand-dot{position:absolute;left:131px;top:30px;width:44px;height:44px;border-radius:50%;background:var(--orange)}
.brand-circle .brand-name{position:absolute;left:0;top:84px;width:100%;font-weight:800;font-size:34px;color:var(--navy);line-height:1}
.brand-circle .invite{position:absolute;left:0;top:170px;width:100%;color:var(--navy);line-height:1.18}
.front .brand-circle .invite{font-size:30px}
.back .brand-circle .invite{font-size:26px;top:178px}
.brand-circle .invite strong{display:block;font-weight:700}
.brand-circle .invite span{display:block;font-weight:500}

.headline{position:absolute;left:59px;color:var(--white);font-weight:900;font-style:italic;line-height:1;letter-spacing:-1px}
.front .headline{top:672px;font-size:80px}
.front .headline span{display:block;margin-bottom:2px}
.back .headline{top:664px}
.back .headline .l1{display:block;font-size:80px}
.back .headline .l2{display:block;font-size:60px;margin-top:2px}

.subhead{position:absolute;left:59px;color:var(--orange-warm);font-weight:600;line-height:1.2}
.front .subhead{top:834px;font-size:46px}
.front .subhead .caps{font-weight:700;font-size:44px}
.back .subhead{top:814px;font-size:48px}
.subhead span{display:block}

.promise{position:absolute;left:59px;color:var(--white);font-weight:500;font-size:20px;line-height:1.65}
.front .promise{top:930px}
.back .promise{top:925px}

.diver-shape{position:absolute;left:62px;top:975px;width:560px;height:180px;border-radius:50%;background:radial-gradient(ellipse at center,rgba(0,60,140,.45) 0%,rgba(0,60,140,0) 70%)}

.lunch{position:absolute;color:var(--white);font-style:italic;font-weight:600;font-size:29px;line-height:1.18}
.front .lunch{left:249px;top:1168px}
.back .lunch{left:238px;top:1160px}
.lunch .hl{color:var(--orange-warm);font-weight:700}
.lunch span{display:block}

.footer{position:absolute;left:0;top:1287px;width:1028px;height:156px;background:var(--navy)}
.footer .foot-brand{position:absolute;left:34px;top:38px;width:150px;height:80px}
.footer .foot-brand .dot{position:absolute;left:52px;top:0;width:40px;height:40px;border-radius:50%;background:var(--orange)}
.footer .foot-brand .name{position:absolute;left:0;top:46px;width:150px;text-align:center;font-weight:800;font-size:22px;color:var(--orange);line-height:1}
.call{position:absolute;left:216px;top:31px;width:274px;height:38px;border-radius:8px;background:var(--orange);color:var(--navy);font-size:24px;font-weight:500;line-height:38px;padding-left:10px;white-space:nowrap}
.call .phone-icon{display:inline-block;vertical-align:middle;margin:0 6px 4px 10px}
.site{position:absolute;left:216px;top:81px;width:622px;height:35px}
.site .site-label{position:absolute;left:0;top:0;width:300px;height:35px;background:var(--orange);clip-path:polygon(0 0,100% 0,calc(100% - 14px) 100%,0 100%);color:var(--navy);font-size:24px;font-weight:500;line-height:35px;padding-left:22px}
.site .site-url{position:absolute;left:284px;top:0;width:338px;height:35px;background:var(--blue-bar);clip-path:polygon(14px 0,100% 0,100% 100%,0 100%);color:var(--white);font-size:24px;font-weight:500;line-height:35px;padding-left:40px}
.contact{position:absolute;left:568px;color:var(--white);font-size:14px;line-height:18px;white-space:nowrap}
.contact.addr{top:27px}
.contact.mail{top:51px}
.contact svg{vertical-align:middle;margin-right:12px;margin-top:-3px}
</style>
</head>
<body>

<div class="side-label front">FRONT</div>

<section class="flyer front">
  <div class="hero-photo" role="img" aria-label="Photo of a calm bay on the north of Bonaire with cactus scrub, hills and a dirt trail under a blue sky"></div>
  <svg class="wave" viewBox="0 0 1028 1443" aria-hidden="true">
    <defs>
      <linearGradient id="sea-front" x1="0" y1="0" x2="0" y2="1">
        <stop offset="0" stop-color="#0a8fd6"/>
        <stop offset="0.45" stop-color="#0677ba"/>
        <stop offset="1" stop-color="#0054aa"/>
      </linearGradient>
    </defs>
    <path d="M0 445 C150 520 250 640 440 632 C560 626 600 470 720 462 C840 455 900 600 1028 612 L1028 1443 L0 1443 Z" fill="#00a9dd"/>
    <path d="M0 470 C150 545 250 665 440 657 C560 650 600 510 720 505 C840 500 900 640 1028 660 L1028 1443 L0 1443 Z" fill="url(#sea-front)"/>
  </svg>
  <div class="photo-circle small" role="img" aria-label="Photo of a rocky coastline with turquoise sea"></div>
  <div class="badge" role="img" aria-label="Dive certification partner badge"></div>

  <div class="brand-circle">
    <div class="brand-dot"></div>
    <div class="brand-name">REEF TRAIL</div>
    <div class="invite"><span>JOIN US ON THE</span><strong>GUIDED DIVES</strong></div>
  </div>

  <h1 class="headline"><span>LET US</span><span>GUIDE YOU!</span></h1>
  <p class="subhead"><span>2 guided dives at the</span><span class="caps">NORTH SIDE OF BONAIRE</span></p>
  <p class="promise">You just enjoy the dives, we take care of the rest<br>We show you the cool stuff</p>
  <div class="diver-shape" role="img" aria-label="Faint silhouette of a scuba diver"></div>

  <div class="photo-circle food" role="img" aria-label="Photo of plates with local lunch: stewed meat, rice, fries and fresh vegetables"></div>
  <p class="lunch"><span>AUTHENTIC</span><span class="hl">LOCAL LUNCH AND DRINKS</span><span>AT CASA VISTA ALTA</span></p>

  <footer class="footer">
    <div class="foot-brand"><div class="dot"></div><div class="name">REEF TRAIL</div></div>
    <div class="call">CALL US<svg class="phone-icon" width="24" height="24" viewBox="0 0 24 24"><circle cx="12" cy="12" r="11" fill="#ffffff"/><path d="M8 6.5c.6-.4 1.2-.2 1.5.3l1 1.8c.3.5.1 1-.3 1.3l-.7.5c.6 1.4 1.6 2.5 3 3.2l.6-.7c.3-.4.9-.5 1.3-.2l1.8 1.1c.5.3.6 1 .2 1.5-1 1.2-2.4 1.4-3.8.7-2.6-1.3-4.5-3.4-5.4-6-.4-1.4 0-2.7.8-3.5z" fill="#3b8fc0"/></svg>(599) 555 01 23</div>
    <div class="site"><div class="site-label">Visit our website</div><div class="site-url">www.reeftrail-dive.com</div></div>
    <div class="contact addr"><svg width="16" height="16" viewBox="0 0 16 16"><circle cx="8" cy="8" r="8" fill="#3b8fc0"/><path d="M8 3.5a3 3 0 0 0-3 3c0 2.2 3 5.5 3 5.5s3-3.3 3-5.5a3 3 0 0 0-3-3zm0 4.2a1.2 1.2 0 1 1 0-2.4 1.2 1.2 0 0 1 0 2.4z" fill="#fff"/></svg>kaya marina 12, Kralendijk, Bonaire</div>
    <div class="contact mail"><svg width="16" height="16" viewBox="0 0 16 16"><circle cx="8" cy="8" r="8" fill="#3b8fc0"/><rect x="4" y="5.2" width="8" height="5.6" rx="0.8" fill="#fff"/><path d="M4.3 5.6L8 8.3l3.7-2.7" fill="none" stroke="#3b8fc0" stroke-width="0.9"/></svg>info@reeftrail-dive.com</div>
  </footer>
</section>

<div class="side-label back">BACK</div>

<section class="flyer back">
  <div class="hero-photo" role="img" aria-label="Photo from under a thatched beach umbrella looking out over a white sand beach, rocks and turquoise sea"></div>
  <svg class="wave" viewBox="0 0 1028 1443" aria-hidden="true">
    <defs>
      <linearGradient id="sea-back" x1="0" y1="0" x2="0" y2="1">
        <stop offset="0" stop-color="#0a8fd6"/>
        <stop offset="0.45" stop-color="#0677ba"/>
        <stop offset="1" stop-color="#0054aa"/>
      </linearGradient>
    </defs>
    <path d="M0 445 C150 520 250 640 440 632 C560 626 600 470 720 462 C840 455 900 600 1028 612 L1028 1443 L0 1443 Z" fill="#00a9dd"/>
    <path d="M0 470 C150 545 250 665 440 657 C560 650 600 510 720 505 C840 500 900 640 1028 660 L1028 1443 L0 1443 Z" fill="url(#sea-back)"/>
  </svg>
  <div class="photo-circle small" role="img" aria-label="Underwater photo of a seahorse holding on to red coral"></div>
  <div class="badge" role="img" aria-label="Dive certification partner badge"></div>

  <div class="brand-circle">
    <div class="brand-dot"></div>
    <div class="brand-name">REEF TRAIL</div>
    <div class="invite"><span>DOE MEE MET DE</span><strong>BEGELEIDE DUIKEN</strong></div>
  </div>

  <h1 class="headline"><span class="l1">LAAT ONS</span><span class="l2">JE BEGELEIDEN!</span></h1>
  <p class="subhead"><span>2 gidsduiken in het</span><span>Noorden van Bonaire</span></p>
  <p class="promise">Wij laten de mooiste dingen zien<br>Geniet van de duiken, wij regelen de rest</p>
  <div class="diver-shape" role="img" aria-label="Faint silhouette of a scuba diver"></div>

  <div class="photo-circle food" role="img" aria-label="Photo of plates with local lunch: stewed meat, rice, fries and fresh vegetables"></div>
  <p class="lunch"><span>AUTHENTIEKE</span><span class="hl">LOKALE LUNCH MET DRANK</span><span>JES BIJ CASA VISTA ALTA</span></p>

  <footer class="footer">
    <div class="foot-brand"><div class="dot"></div><div class="name">REEF TRAIL</div></div>
    <div class="call">CALL US<svg class="phone-icon" width="24" height="24" viewBox="0 0 24 24"><circle cx="12" cy="12" r="11" fill="#ffffff"/><path d="M8 6.5c.6-.4 1.2-.2 1.5.3l1 1.8c.3.5.1 1-.3 1.3l-.7.5c.6 1.4 1.6 2.5 3 3.2l.6-.7c.3-.4.9-.5 1.3-.2l1.8 1.1c.5.3.6 1 .2 1.5-1 1.2-2.4 1.4-3.8.7-2.6-1.3-4.5-3.4-5.4-6-.4-1.4 0-2.7.8-3.5z" fill="#3b8fc0"/></svg>(599) 555 01 23</div>
    <div class="site"><div class="site-label">Visit our website</div><div class="site-url">www.reeftrail-dive.com</div></div>
    <div class="contact addr"><svg width="16" height="16" viewBox="0 0 16 16"><circle cx="8" cy="8" r="8" fill="#3b8fc0"/><path d="M8 3.5a3 3 0 0 0-3 3c0 2.2 3 5.5 3 5.5s3-3.3 3-5.5a3 3 0 0 0-3-3zm0 4.2a1.2 1.2 0 1 1 0-2.4 1.2 1.2 0 0 1 0 2.4z" fill="#fff"/></svg>kaya marina 12, Kralendijk, Bonaire</div>
    <div class="contact mail"><svg width="16" height="16" viewBox="0 0 16 16"><circle cx="8" cy="8" r="8" fill="#3b8fc0"/><rect x="4" y="5.2" width="8" height="5.6" rx="0.8" fill="#fff"/><path d="M4.3 5.6L8 8.3l3.7-2.7" fill="none" stroke="#3b8fc0" stroke-width="0.9"/></svg>info@reeftrail-dive.com</div>
  </footer>
</section>

</body>
</html>
```